Kestrel Building Works Business Card and more!

We need a business card design for Kestrel Building Works Ltd, a respected building company that specialises in high quality designer homes.

We're after a sleek, clean, modern business card that incorporates our new logo (see attached) and colours, with black being the background.

We are Certified Framing Guild and need to include their logo (see attached) on our cards, balancing but not taking over our logo.

Details to be included:

Malcolm Tivey
Director

Phone: 0218845126
Email: kestrelbuild.nz@maildrop-example.co.nz
Website: www.kestrelbuildingworks-example.co.nz

Additional Information

A start up website is also under construction and needing attention and letterheads are needed!

We look forward to your designs!

Target Market(s)

30+ people who are interested in building new or renovating current homes

Industry/Entity Type

Construction

Contact Information for Business Card

Malcolm Tivey
Director

Phone: 0218845126
Facebook: www.socialpage-example.com/kestrelbuild.nz

Font styles to use
Serif

Colors

Designer to choose colors to be used in the design.

Requirements
Must have
• Our new logo
• Our colours
• cfg logo

```html
<!DOCTYPE html>
<html lang="en">
<head>
<meta charset="utf-8">
<title>Kestrel Building Works – Letterhead</title>
<link rel="stylesheet" href="https://fonts.googleapis.com/css2?family=Cinzel:wght@500&family=Montserrat:wght@400;500&display=swap">
<style>
  :root {
    --backdrop: #b9b8b4;
    --paper: #ffffff;
    --ink: #1f1f1f;
    --ink-soft: #4a4a4a;
    --brand-dark: #2a2a2a;
    --gold: #c49a5e;
    --band-black: #111111;
  }
  * { margin: 0; padding: 0; box-sizing: border-box; }
  html, body {
    width: 1200px;
    height: 1084px;
    overflow: hidden;
    background: var(--backdrop);
  }
  .letterhead {
    position: absolute;
    left: 231px;
    top: 17px;
    width: 738px;
    height: 1050px;
    background: var(--paper);
    font-family: "Montserrat", Arial, sans-serif;
    color: var(--ink);
  }
  .brand {
    position: absolute;
    top: 60px;
    left: 0;
    width: 100%;
    text-align: center;
  }
  .brand-name {
    font-family: "Cinzel", Georgia, serif;
    font-weight: 500;
    font-size: 28px;
    letter-spacing: 2px;
    color: var(--brand-dark);
  }
  .letter {
    position: absolute;
    left: 70px;
    top: 218px;
    width: 612px;
    font-size: 12.6px;
    line-height: 15px;
  }
  .recipient { margin-bottom: 30px; }
  .letter p { margin-bottom: 15px; text-align: left; }
  .salutation-line { margin-bottom: 0; }
  .closing { margin-top: 8px; }
  .signature {
    display: block;
    width: 130px;
    height: 30px;
    margin-top: 24px;
    background: linear-gradient(90deg, #e9e9e9, #f4f4f4);
    border-radius: 3px;
  }
  .signer-title { margin-top: 6px; }
  .contact-line {
    position: absolute;
    left: 0;
    top: 1014px;
    width: 100%;
    text-align: center;
    font-size: 11px;
    color: var(--ink-soft);
  }
  .contact-line .divider { margin: 0 8px; }
  .footer-band {
    position: absolute;
    left: 0;
    bottom: 0;
    width: 100%;
    height: 8px;
    display: flex;
  }
  .footer-band .band-black { width: 562px; background: var(--band-black); }
  .footer-band .band-gold { flex: 1; background: var(--gold); }
</style>
</head>
<body>
  <main class="letterhead">
    <header class="brand">
      <div class="brand-name">Kestrel Building Works</div>
    </header>

    <section class="letter">
      <div class="recipient">
        November 1, 2015<br>
        Mr. Owen Barlow<br>
        58 Harbour Row Lane<br>
        Dunmore, U.K 40712
      </div>

      <div class="salutation-line">Dear Mr. Barlow</div>
      <p>The first paragraph of a typical business letter is used to state the main point of the letter. Begin with a friendly opening, then quickly transition into the purpose of your letter. Use a couple of sentences to explain the purpose, but do not go in to detail until the next paragraph.</p>
      <p>Beginning with the second paragraph, state the supporting details to justify your purpose. These may take the form of background information, statistics or first-hand accounts. A few short paragraphs within the body of the letter should be enough to support your reasoning. Finally, in the closing paragraph, briefly restate your purpose and why it is important. If the purpose of your letter is related to your employment, consider ending your letter with your contact information and title if it not included on letterhead.</p>
      <p>Finally, in the closing paragraph, briefly restate your purpose and why it is important. If the purpose of your letter is related to your employment, consider ending your letter with your contact information and title if it not included on letterhead.</p>
      <p>Finally, in the closing paragraph, briefly restate your purpose and why it is important. If the purpose of your letter is related to your employment, consider ending your letter with your contact information and title if it not included on letterhead.</p>
      <p>Finally, in the closing paragraph, briefly restate your purpose and why it is important. If the purpose of your letter is related to your employment, consider ending your letter with your contact information and title if it not included on letterhead. Finally, in the closing paragraph, briefly restate your purpose and why it is important. If the purpose of your letter is related to your employment, consider ending your letter with your contact information and title if it not included on letterhead.</p>
      <p>Finally, in the closing paragraph, briefly restate your purpose and why it is important. If the purpose of your letter is related to your employment, consider ending your letter with your contact information and title if it not included on letterhead. However, if the purpose is informational, think about closing with gratitude for the reader's time.</p>

      <div class="closing">Sincerely,</div>
      <span class="signature" role="img" aria-label="Handwritten signature of the company president"></span>
      <div class="signer-title">President</div>
    </section>

    <footer>
      <div class="contact-line">
        0218845126<span class="divider">|</span>kestrelbuild.nz@maildrop-example.co.nz<span class="divider">|</span>www.kestrelbuildingworks-example.co.nz
      </div>
      <div class="footer-band">
        <div class="band-black"></div>
        <div class="band-gold"></div>
      </div>
    </footer>
  </main>
</body>
</html>
```